Copperfield Capital Partners Web Design

Copperfield Capital Partners is a national strategic business consulting company serving both marijuana businesses and investors. We assist emerging businesses in the marijuana sector that need assistance in developing their brand awareness and investor visibility within the industry. In addition, we provide information about these companies to investors so the can make financial decisions and discuss them in our forums. We would like to see designs that use the colors green, black and grey but please feel free to use your imagination. The final design should communicate financial growth

Target Market(s)

21-55+ men willing to invest in the marijuana market. These are savvy people who are expect to see a professional website.

Industry/Entity Type

Business

Coding

Coded - Design and coding required

Number of Pages Required

5+ page

Font styles to use
Serif
Sans Serif

Colors
abd036
cadf82
9bcb3c
c3c3c3
ffffff
000000

Requirements
Must have
• A Homepage, About Us page, Contact Us page, Watch List, Forums, a Disclaimer page, Privacy Policy and a "Watch List" page for us to promote marijuana companies on. We need a section to ask for visitor email addresses to join our mailing list. The site must be simple to navigate, but professional. If you were going to invest money into a risky marijuana market, what kind of website would you trust to get your information from?
Nice to have
• Our Facebook and Twitter integrated:
• www.facebook.com/CopperfieldCapitalPartners
• twitter.com/CopperfieldCP
• It would be nice if we could have a rolling comments section, where visitors can use facebook or whatever to post a quick comment. Maybe a testimonials page.
• It would be nice to have a blog page.

```html
<!DOCTYPE html>
<html lang="en">
<head>
<meta charset="utf-8">
<title>Copperfield Capital Partners</title>
<link rel="stylesheet" href="https://fonts.googleapis.com/css2?family=Tinos:ital,wght@0,400;0,700;1,400&family=Lato:wght@400;700&family=Arimo:wght@400;700&display=swap">
<style>
:root{
  --green:#6a9a2a;
  --green-light:#abd036;
  --ink:#000;
  --dark:#111;
  --footer:#0b0b0b;
  --grey:#c3c3c3;
  --text:#666;
  --soft:#f7f7f7;
  --white:#fff;
}
*{margin:0;padding:0;box-sizing:border-box}
html,body{width:1066px;height:1200px;overflow:hidden;background:var(--white)}
body{position:relative;font-family:"Arimo",Arial,sans-serif;color:var(--text)}
a{text-decoration:none;color:inherit}

/* header */
.site-header{position:absolute;top:0;left:0;width:1066px;height:58px;background:var(--white)}
.brand{position:absolute;left:228px;top:12px;display:flex;align-items:center;gap:8px}
.brand-mark{width:12px;height:12px;background:var(--green)}
.brand-name{font-family:"Lato",sans-serif;font-weight:700;font-size:18px;color:var(--green);letter-spacing:.5px}
.main-nav{position:absolute;right:212px;top:17px;display:flex;gap:22px;font-family:"Tinos",serif;font-size:11px;color:#555}
.main-nav .active{color:var(--green)}

/* hero */
.hero{position:absolute;top:58px;left:0;width:1066px;height:260px;
  background:radial-gradient(ellipse 380px 170px at 700px 170px,#7c8f1c 0%,#3f4a12 40%,#141410 75%),#111}
.hero-title{position:absolute;left:226px;top:112px;font-family:"Tinos",serif;font-weight:700;color:var(--white);line-height:1}
.hero-title .l1{display:block;font-size:25px}
.hero-title .l2{display:block;font-size:17.5px;margin-top:4px}
.slider-dots{position:absolute;left:529px;top:224px;display:flex;gap:3px}
.slider-dots span{width:6px;height:6px;border-radius:50%;background:var(--white)}
.slider-dots span:first-child{background:var(--green-light)}

/* offer */
.offer{position:absolute;top:318px;left:0;width:1066px;height:208px;background:var(--soft)}
.section-title{position:absolute;top:40px;left:228px;width:626px;height:20px;display:flex;align-items:center;justify-content:center}
.section-title::before,.section-title::after{content:"";flex:1;height:1px;background:#ddd}
.section-title h2{font-family:"Lato",sans-serif;font-weight:400;font-size:17px;color:#555;padding:0 22px;position:relative}
.section-title h2::before,.section-title h2::after{content:"";position:absolute;top:8px;width:5px;height:5px;border-radius:50%;background:#ccc}
.section-title h2::before{left:-2px}.section-title h2::after{right:-2px}
.services{position:absolute;top:87px;left:228px;width:660px;display:grid;grid-template-columns:167px 165px 160px 160px}
.service h3{display:flex;align-items:center;gap:8px;font-family:"Lato",sans-serif;font-weight:400;font-size:12.5px;color:var(--green)}
.service h3 .num{width:20px;height:20px;border:1px solid var(--green);border-radius:50%;font-size:10px;display:flex;align-items:center;justify-content:center}
.service p{margin-top:11px;font-family:"Tinos",serif;font-size:10px;line-height:1.1;color:#555}
.service .more{display:block;margin-top:12px;font-size:6px;color:#888}

/* welcome */
.welcome{position:absolute;top:526px;left:0;width:1066px;height:242px;background:var(--white)}
.welcome-art{position:absolute;left:228px;top:44px;width:192px;height:132px;border-radius:8px;
  background:linear-gradient(160deg,#e9efe0 0%,#c7d99a 50%,#f3f3f3 100%)}
.welcome-text{position:absolute;left:464px;top:36px;width:392px}
.welcome-text h2{font-family:"Lato",sans-serif;font-weight:400;font-size:16px;color:#555}
.welcome-text h2 b{font-weight:700}
.tagline{margin-top:14px;font-family:"Tinos",serif;font-size:12.5px;color:#555;line-height:1.15}
.tagline span{display:block;color:var(--green)}
.sub{margin-top:14px;font-family:"Tinos",serif;font-style:italic;font-size:10.5px;color:#777}
.welcome-text .body{margin-top:9px;font-size:7.2px;line-height:12.9px;color:#888}

/* green band */
.band{position:absolute;top:768px;left:0;width:1066px;height:235px;
  background:linear-gradient(90deg,#4f8a1c 0%,#5f9a26 40%,#64a02a 100%)}
.blog{position:absolute;left:228px;top:2px;width:210px;height:232px;background:var(--dark);color:var(--white);padding:20px 14px}
.blog h3{text-align:center;font-family:"Lato",sans-serif;font-weight:400;font-size:10px;letter-spacing:.3px}
.blog h3 b{font-weight:700}
.post{display:flex;gap:10px;margin-top:20px;padding-bottom:16px;border-bottom:1px solid #333}
.post+.post{margin-top:16px;border-bottom:0}
.thumb{width:71px;height:53px;flex:none;background:linear-gradient(135deg,#d8e6f2,#5b86b5)}
.post h4{font-size:7.3px;font-weight:700;line-height:1.25}
.post .date{display:flex;align-items:center;gap:4px;margin-top:6px;font-size:6px;font-weight:700;color:var(--green-light)}
.post .date i{width:6px;height:5px;background:var(--green-light)}
.post p{margin-top:6px;font-size:6.5px;color:#aaa;line-height:1.4}
.testimonial{position:absolute;left:488px;top:52px;width:376px}
.avatar{position:absolute;left:0;top:0;width:53px;height:53px;border-radius:50%;border:2px solid var(--white);background:linear-gradient(#e3e3e3,#7d7d7d)}
.quote{position:absolute;left:76px;top:0;width:300px;font-size:8px;font-weight:700;color:var(--white);line-height:1.55}
.cite{position:absolute;left:76px;top:54px;font-size:8px;font-weight:700;color:var(--white);white-space:nowrap}
.cite em{font-weight:400}
.quote-dots{position:absolute;left:78px;top:90px;display:flex;gap:3px}
.quote-dots span{width:5px;height:5px;border-radius:50%;background:var(--ink)}
.quote-dots span:first-child{background:var(--white)}

/* tweet bar */
.tweet-bar{position:absolute;top:1003px;left:0;width:1066px;height:43px;background:var(--footer)}
.tweet{position:absolute;left:228px;top:16px;width:626px;display:flex;align-items:center;font-size:8px;color:#ccc}
.tweet .icon{width:12px;height:12px;border-radius:50%;background:var(--green);margin-right:34px}
.tweet a{color:var(--green-light);font-weight:700;margin-left:5px}
.tweet time{margin-left:auto;font-style:italic;color:#999}
.tweet-bar::after{content:"";position:absolute;left:228px;right:212px;bottom:0;height:1px;background:#2a2a2a}

/* footer */
.site-footer{position:absolute;top:1046px;left:0;width:1066px;height:154px;background:var(--footer);color:#aaa}
.foot-brand{position:absolute;left:228px;top:30px;font-family:"Lato",sans-serif;font-weight:700;font-size:13px;color:var(--white)}
.copy{position:absolute;left:228px;top:68px;font-size:7px;color:#999}
.foot-links{position:absolute;left:455px;top:34px}
.foot-links h4,.mailing h4{font-size:7.5px;font-weight:700;color:var(--white);letter-spacing:.3px}
.foot-links ul{list-style:none;margin-top:13px;font-size:7.2px;line-height:15.6px;color:#aaa}
.mailing{position:absolute;left:587px;top:34px;width:267px}
.signup{display:flex;margin-top:10px;height:27px}
.signup input{flex:1;border:0;background:#555;color:#ddd;font:7px "Arimo",sans-serif;padding-left:12px}
.signup input::placeholder{color:#ddd}
.signup button{width:42px;border:0;background:var(--green);display:flex;align-items:center;justify-content:center}
.follow{margin-top:14px}
.social{display:flex;gap:8px;margin-top:10px}
.social span{width:16px;height:16px;border-radius:50%;background:#666}
</style>
</head>
<body>

<header class="site-header">
  <a class="brand" href="#"><span class="brand-mark"></span><span class="brand-name">Copperfield Capital Partners</span></a>
  <nav class="main-nav">
    <a class="active" href="#">Home</a><a href="#">About Us</a><a href="#">Watch List</a><a href="#">Forums</a><a href="#">Contact Us</a>
  </nav>
</header>

<section class="hero" role="img" aria-label="Young green seedling growing from dark soil">
  <h1 class="hero-title"><span class="l1">EVERYTHING YOU NEED</span><span class="l2">TO KNOW ABOUT BUSINESS</span></h1>
  <div class="slider-dots"><span></span><span></span><span></span></div>
</section>

<section class="offer">
  <div class="section-title"><h2>WHAT WE OFFER</h2></div>
  <div class="services">
    <div class="service"><h3><span class="num">1</span>Strategic Business</h3><p>Praesent vestibulum molestie lacus.<br>Aenean nonummy</p><a class="more" href="#">READ MORE</a></div>
    <div class="service"><h3><span class="num">2</span>Finance Management</h3><p>Praesent vestibulum molestie lacus.<br>Aenean nonummy</p><a class="more" href="#">READ MORE</a></div>
    <div class="service"><h3><span class="num">3</span>Consulting Services</h3><p>Praesent vestibulum molestie lacus.<br>Aenean nonummy</p><a class="more" href="#">READ MORE</a></div>
    <div class="service"><h3><span class="num">4</span>Investor Visibility</h3><p>Praesent vestibulum molestie lacus.<br>Aenean nonummy</p><a class="more" href="#">READ MORE</a></div>
  </div>
</section>

<section class="welcome">
  <div class="welcome-art" role="img" aria-label="Illustration of a rising bar chart with a green growth arrow over papers"></div>
  <div class="welcome-text">
    <h2><b>WELCOME</b> TO COPPERFIELD CAPITAL PARTNERS!</h2>
    <p class="tagline">We represent a huge experience &amp; outstanding<span>INTELLECTUAL POTENTIAL.</span></p>
    <p class="sub">Sit consectetuer adipiscing praesent vestibulum aenean nonummy hendrerit.</p>
    <p class="body">Lorem Ipsum is simply dummy text of the printing and typesetting industry. Lorem Ipsum has been the industry's standard dummy text ever since the 1500s, when an unknown printer took a galley of type and scrambled it to make a type specimen book. It has survived not only five centuries, but also the leap into electronic typesetting, remaining essentially unchanged. It was popularised in the 1960s with the release of Inkline sheets containing Lorem Ipsum passages, and more recently with desktop publishing software like Pagecraft Studio including versions of Lorem Ipsum.</p>
  </div>
</section>

<section class="band" role="img" aria-label="Green-tinted photo of a modern meeting room">
  <div class="blog">
    <h3><b>LATEST</b> BLOG</h3>
    <article class="post">
      <div class="thumb" role="img" aria-label="Financial charts and documents"></div>
      <div><h4>Duis aute irure dolor in reprehenderit in voluptate</h4><p class="date"><i></i>16 May, 2015</p><p>Lorem ipsum dolor sit amet, consectetur adipiscing elit</p></div>
    </article>
    <article class="post">
      <div class="thumb" role="img" aria-label="Glass office towers against the sky"></div>
      <div><h4>Duis aute irure dolor in reprehenderit in voluptate</h4><p class="date"><i></i>16 May, 2015</p><p>Lorem ipsum dolor sit amet, consectetur adipiscing elit</p></div>
    </article>
  </div>
  <div class="testimonial">
    <div class="avatar" role="img" aria-label="Portrait of the client giving the testimonial"></div>
    <p class="quote">Duis aute irure dolor in reprehenderit in voluptate velit esse cillum dolore eu fugiat nulla pariatur. Excepteur sint occaecat cupidatat non proident, sunt in culpa qui officia deserunt mollit anim id est laborum.</p>
    <p class="cite">Daren Colby, <em>Company Name</em></p>
    <div class="quote-dots"><span></span><span></span><span></span><span></span></div>
  </div>
</section>

<div class="tweet-bar">
  <p class="tweet"><span class="icon"></span>Duis aute irure dolor in reprehenderit in voluptate velit esse cillum dolore eu fugiat nulla pariatur.<a href="#">cpcp.link/n/48213</a><time>2min ago</time></p>
</div>

<footer class="site-footer">
  <div class="foot-brand">Copperfield Capital Partners</div>
  <p class="copy">Copyright © 2015 | Disclaimer &nbsp;|&nbsp; Privacy Policy</p>
  <nav class="foot-links">
    <h4>SITE LINKS</h4>
    <ul><li>Home</li><li>About Us</li><li>Watch List</li><li>Forums</li><li>Contact Us</li></ul>
  </nav>
  <div class="mailing">
    <h4>JOIN OUR MAILING LIST</h4>
    <form class="signup"><input type="email" placeholder="Your Email Address"><button type="button" aria-label="Subscribe"><svg width="8" height="12" viewBox="0 0 8 12"><path d="M1 1l5 5-5 5" fill="none" stroke="#fff" stroke-width="1.5"/></svg></button></form>
    <h4 class="follow">FOLLOW US</h4>
    <div class="social"><span></span><span></span><span></span></div>
  </div>
</footer>

</body>
</html>
```